Wine Label Design for a white wine made in the region of San Gimignano, Italy

This is a white wine (crisp and fresh) that is made in the region of San Gimignano, Italy, which is a beautiful hill town in Tuscany famous for it's towers. We would like a classy, elegant front wine label that can also be somewhat fun and whimsical if you prefer. Showcasing or depicting or alluding to the town and the towers of San Gimignano is a plus. The label should state the brand name which is "Vellisora", the varietal, which is Vernaccia di San Gimignano, and the vintage which is 2015. We might change the size of the label slightly but for design purposes please use 5 inches wide x 5 1/2 inches tall. I've uploaded a photo of a successful label design for parameters, but you should not feel limited to this either. Good white wine colors are white and green but we are flexible. Please don't use red, burgundy, or blue colors.

Target Market(s)

This wine label should appeal to all ages but be classy for the older crowd and still eye catching and fun for the millennials. This wine is sold in 15 states in the US, on the East Coast.

Industry/Entity Type

Town

Font styles to use
Serif
Sans Serif

Requirements
Must have
• Referring somehow or depicting the hill town and towers of San Gimignano in some way, such as in silhouette would be a plus. But also try to do something fun and unique with it-- not just an image of the town with words placed over it.
Should not have
• Please don't use the colors blue, reds. Try to think about what makes a wine label classy and sophisticated and 'upmarket' and what makes one cheap and cheesy. We are looking for the classy and sophisticated.

```html
<!DOCTYPE html>
<html lang="en">
<head>
<meta charset="utf-8">
<title>Vellisora – Vernaccia di San Gimignano</title>
<link rel="stylesheet" href="https://fonts.googleapis.com/css2?family=Cinzel:wght@500;600&family=Raleway:wght@200;300&display=swap">
<style>
  :root {
    --page-bg: #ffffff;
    --label-bg: #ffffff;
    --label-border: #4a4a4a;
    --olive: #7c8a3e;
    --copper-dark: #8a4f1e;
    --copper: #c07a3a;
    --gold-light: #f3de8a;
    --cream: #f7f4e6;
    --cream-warm: #efe3c4;
  }
  * { margin: 0; padding: 0; box-sizing: border-box; }
  html, body {
    width: 1200px;
    height: 1000px;
    overflow: hidden;
    background: var(--page-bg);
  }
  .canvas {
    position: relative;
    width: 1200px;
    height: 1000px;
  }
  .label {
    position: absolute;
    left: 307px;
    top: 178px;
    width: 586px;
    height: 644px;
    background: var(--label-bg);
    border: 1px solid var(--label-border);
  }
  .brand-name {
    position: absolute;
    top: 92px;
    left: 0;
    width: 100%;
    text-align: center;
    font-family: "Raleway", sans-serif;
    font-weight: 300;
    font-size: 49px;
    letter-spacing: 1px;
    line-height: 1;
    color: var(--olive);
  }
  .gold-rule {
    position: absolute;
    top: 154px;
    left: 101px;
    width: 384px;
    height: 8px;
    background: linear-gradient(90deg, var(--copper) 0%, var(--copper-dark) 22%, var(--gold-light) 38%, var(--copper) 58%, var(--copper-dark) 78%, var(--copper) 90%, var(--copper-dark) 100%);
  }
  .town-scene {
    position: absolute;
    top: 183px;
    left: 101px;
    width: 384px;
    height: 228px;
    background:
      linear-gradient(180deg, rgba(247,244,230,1) 0%, rgba(247,244,230,0) 30%),
      linear-gradient(90deg, var(--cream-warm) 0%, #d9b27a 35%, #b87a40 60%, #c99868 80%, var(--cream-warm) 100%);
  }
  .varietal {
    position: absolute;
    top: 432px;
    left: 0;
    width: 100%;
    text-align: center;
    font-family: "Cinzel", serif;
    font-weight: 600;
    color: var(--olive);
    line-height: 1;
  }
  .varietal-line {
    display: block;
    font-size: 36px;
    letter-spacing: 0.5px;
  }
  .varietal-joiner {
    display: block;
    font-size: 15px;
    margin: 4px 0 6px;
    font-weight: 500;
  }
  .vintage {
    position: absolute;
    top: 552px;
    left: 0;
    width: 100%;
    text-align: center;
    font-family: "Raleway", sans-serif;
    font-weight: 300;
    font-size: 40px;
    line-height: 1;
    color: var(--olive);
  }
</style>
</head>
<body>
  <main class="canvas">
    <section class="label">
      <h1 class="brand-name">VELLISORA</h1>
      <div class="gold-rule"></div>
      <div class="town-scene" role="img" aria-label="Copper and gold sketch of the hill town of San Gimignano with its stone buildings, towers, arched gate and cypress trees"></div>
      <h2 class="varietal">
        <span class="varietal-line">Vernaccia</span>
        <span class="varietal-joiner">DI</span>
        <span class="varietal-line">San Gimignano</span>
      </h2>
      <p class="vintage">2016</p>
    </section>
  </main>
</body>
</html>
```